Summit Paths Business Needs A Study Guide Design

We need a booklet design for our Case Study that will be online for free download to our users. In addition the overall layout and look and feel of the guide should compliment the cover design. We're a new company based in Australia known as Bright Quarry and we provide free career tools and insights to young professionals. Please see attached examples x4 of guides/booklet designs we like. Please build design to include a cover page, contents page, introduction page and business lessons section. This is not showcased in the current content.

We would like to see designs that use our corporate colours, appealing to the eye layout and ooze professionalism whilst not being too corporate and having a trendiness that 20-30 year olds would like.

The case is study is the story of Zelto titled The Coinfree Ride: Zelto - the app that connects drivers to users and essentially has replaced taxis. Some suggested images are attached but we welcome your thoughts and others for consideration.

The guide reads like a story so the final design should communicate a business education. The chosen designer will be asked to design several other case studies and career guides in the next few months.

Require in locked PDF
Updates

Hi All, Please see the updated brief as well as 4x attachments of booklet designs we like. So far all submissions have only included a cover page. We would like to see the full layout. Thanks, Megan

Target Market(s)

20-30 year olds

Industry/Entity Type

Business

Font styles to use
Sans Serif

Requirements
Must have
• Bright Quarry Logo
• All hyperlinks remain in place.
• Bright Quarry corporate colours:
• Options of 3.
• Grey R66 G73 B74
• White R242 G240 B230
• Teal R38 G128 B138
• PLEASE VIEW EXAMPLES OF GUIDES IN THE ATTACHMENTS.
Nice to have
• Certain lines drawn attention to if it looks appealing to the reader and makes sense for the story.
Should not have
• Background colours as some users will download and print.

```html
<!DOCTYPE html>
<html lang="en">
<head>
<meta charset="utf-8">
<title>Contents – The Coinfree Ride Story: Zelto</title>
<link href="https://fonts.googleapis.com/css2?family=Lato:wght@300;400&display=swap" rel="stylesheet">
<style>
  :root {
    --teal: #4f9aa0;
    --ink: #000000;
    --slate: #3f4647;
    --sand: #f0eee6;
    --paper: #ffffff;
    --folio: #555b5c;
  }
  html, body {
    margin: 0;
    padding: 0;
    overflow: hidden;
    background: var(--paper);
  }
  .page {
    position: relative;
    width: 846px;
    height: 1200px;
    box-sizing: border-box;
    border: 1px solid var(--ink);
    background: var(--paper);
    overflow: hidden;
    font-family: "Lato", sans-serif;
  }
  .page-art {
    position: absolute;
    inset: 0;
  }
  .section-title {
    position: absolute;
    left: 3px;
    top: 122px;
    width: 303px;
    height: 124px;
    background: var(--teal);
    color: var(--paper);
    font-weight: 300;
    font-size: 55px;
    line-height: 124px;
    padding-left: 5px;
    box-sizing: border-box;
    margin: 0;
    letter-spacing: 0;
    white-space: nowrap;
  }
  .contents-panel {
    position: absolute;
    left: 311px;
    top: 277px;
    width: 529px;
    height: 369px;
    background: var(--teal);
  }
  .contents-list {
    list-style: none;
    margin: 0;
    padding: 61px 0 0 24px;
    color: var(--paper);
    font-weight: 300;
    font-size: 32px;
    line-height: 42.6px;
    letter-spacing: 1.6px;
    white-space: nowrap;
  }
  .folio {
    position: absolute;
    right: 10px;
    top: 1092px;
    font-size: 26px;
    font-weight: 300;
    color: var(--folio);
  }
  .running-foot {
    position: absolute;
    right: 10px;
    top: 1144px;
    font-size: 17px;
    font-weight: 400;
    letter-spacing: 1px;
    color: var(--paper);
    white-space: nowrap;
  }
</style>
</head>
<body>
  <div class="page">
    <svg class="page-art" width="846" height="1200" viewBox="0 0 846 1200" aria-hidden="true">
      <polygon class="header-wedge" points="0,29 846,29 846,32 0,71" fill="var(--sand)"/>
      <rect class="title-rule" x="306" y="113" width="4" height="141" fill="var(--ink)"/>
      <rect class="panel-rule" x="306" y="269" width="5" height="386" fill="var(--ink)"/>
      <polygon class="footer-wedge" points="0,1168 846,1131 846,1172 0,1172" fill="var(--slate)"/>
    </svg>

    <h1 class="section-title">CONTENTS</h1>

    <nav class="contents-panel">
      <ol class="contents-list">
        <li>1. Company Background</li>
        <li>2. The Taxi Industry</li>
        <li>3. Disruption Impact</li>
        <li>4. Brand Image</li>
        <li>5. Toeing the line</li>
        <li>6. A Zelto Future</li>
      </ol>
    </nav>

    <div class="folio">2.</div>
    <div class="running-foot">The Coinfree Ride Story: Zelto</div>
  </div>
</body>
</html>
```